beauty/party

I have both my designs from artfolk hub. double sided business card needed and incorporate other information. although I have my designs I don't do things by halves so im wanting people to say nice cards. first impression best impression. On the Harbourline roaming glow and care side I want in bullet point the following: Facials, Microdermabrasion, Oxygen Infusion, Peels, Dermaroller . tinting & Adult Pamper Parties. I also want the healthier looking skin removed!! and I want the words love your skin wth a Heart with the word love in it. but not under my logo. somewhere else. If possible!! On the Lady Velvet Wren side I want the words Childrens Pamper, Ballet, Hip Hop & High Tea Parties. I need the number 0438 51 7604 used on both sides and www.ladyvelvetwren.com.au on lady velvet wren side. If you don't understand my instructions you are welcome to message me. Please use the white background

Industry/Entity Type

Graphic Design

```html
<!DOCTYPE html>
<html lang="en">
<head>
<meta charset="utf-8">
<title>Lady Velvet Wren — Business Card</title>
<link rel="stylesheet" href="https://fonts.googleapis.com/css2?family=Arimo:wght@400;700&display=swap">
<style>
  :root {
    --paper: #ffffff;
    --ink: #1a1a1a;
    --pink: #e6197d;
    --yellow: #fff200;
    --stripe-dark: #111111;
    --arch-line: #c9c9c9;
    --dot: #8a8a8a;
  }
  html, body {
    margin: 0;
    padding: 0;
    overflow: hidden;
    background: var(--paper);
  }
  .card {
    position: relative;
    width: 802px;
    height: 1200px;
    background: var(--paper);
    overflow: hidden;
    font-family: "Arimo", Arial, sans-serif;
    color: var(--ink);
  }
  .arch {
    position: absolute;
    left: 52px;
    top: 8px;
    width: 698px;
    height: 1100px;
    border: 3px solid var(--arch-line);
    border-bottom: none;
    border-radius: 349px 349px 0 0 / 260px 260px 0 0;
    box-sizing: border-box;
  }
  .brand {
    position: absolute;
    left: 120px;
    top: 190px;
    width: 560px;
    display: flex;
    align-items: center;
    gap: 22px;
  }
  .brand-name {
    margin: 0;
    font-size: 62px;
    font-weight: 700;
    line-height: 1;
    color: var(--pink);
    letter-spacing: -0.5px;
  }
  .brand-dot {
    width: 70px;
    height: 70px;
    border-radius: 50%;
    background: var(--yellow);
    flex: none;
  }
  .brand-rule {
    position: absolute;
    left: 120px;
    top: 340px;
    width: 535px;
    height: 5px;
    background: var(--pink);
  }
  .phone {
    position: absolute;
    left: 0;
    top: 362px;
    width: 802px;
    text-align: center;
    font-size: 30px;
    margin: 0;
  }
  .services {
    position: absolute;
    left: 155px;
    top: 529px;
    width: 492px;
    height: 492px;
  }
  .services svg { display: block; }
  .service-list {
    position: absolute;
    inset: 0;
    margin: 0;
    padding: 0;
    list-style: none;
  }
  .service-list li {
    position: absolute;
    left: 0;
    width: 100%;
    text-align: center;
    font-size: 27px;
    line-height: 1;
    transform: translateY(-50%);
  }
  .service-list .on-dark { color: var(--yellow); }
  .service-list .on-light { color: var(--stripe-dark); }
  .footer-band {
    position: absolute;
    left: 0;
    top: 1082px;
    width: 802px;
    height: 108px;
    background: var(--pink);
  }
  .footer-strip {
    position: absolute;
    left: 0;
    top: 1114px;
    width: 802px;
    height: 38px;
    background: var(--paper);
    display: flex;
    align-items: center;
    justify-content: center;
  }
  .website {
    font-size: 26px;
    color: var(--ink);
    margin: 0;
  }
</style>
</head>
<body>
  <main class="card">
    <div class="arch"></div>

    <header class="brand">
      <h1 class="brand-name">Lady Velvet Wren</h1>
      <span class="brand-dot" aria-hidden="true"></span>
    </header>
    <div class="brand-rule"></div>
    <p class="phone">0438 51 7604</p>

    <section class="services">
      <svg width="492" height="492" viewBox="0 0 492 492" aria-hidden="true">
        <defs>
          <clipPath id="service-disc"><circle cx="246" cy="246" r="246"/></clipPath>
        </defs>
        <g clip-path="url(#service-disc)">
          <rect x="0" y="0" width="492" height="112" fill="var(--stripe-dark)"/>
          <rect x="0" y="112" width="492" height="112" fill="var(--yellow)"/>
          <rect x="0" y="224" width="492" height="107" fill="var(--stripe-dark)"/>
          <rect x="0" y="331" width="492" height="103" fill="var(--yellow)"/>
          <rect x="0" y="434" width="492" height="58" fill="var(--stripe-dark)"/>
        </g>
        <circle cx="206" cy="462" r="4" fill="var(--dot)"/>
        <circle cx="246" cy="464" r="4" fill="var(--dot)"/>
        <circle cx="286" cy="462" r="4" fill="var(--dot)"/>
      </svg>
      <ul class="service-list">
        <li class="on-dark" style="top:56px">Childrens Pamper</li>
        <li class="on-light" style="top:168px">Ballet</li>
        <li class="on-dark" style="top:278px">Hip Hop</li>
        <li class="on-light" style="top:382px">High Tea Parties</li>
      </ul>
    </section>

    <footer>
      <div class="footer-band"></div>
      <div class="footer-strip">
        <p class="website">www.ladyvelvetwren.com.au</p>
      </div>
    </footer>
  </main>
</body>
</html>
```